Halvard Hubs Business card

Halvard Hubs is a custom bicycle wheel builder. my current website can be viewed at www.halvardhubs.us
design features i am looking for include:
Logo with font used on website(911 porsche) with a gear graphic two meshed gears maybe
black background bright green logo and name
info to include:
front
Lemuel Castaby : owner/builder
ph; 555-418-7290
email sales@halvardhubs.us
www.halvardhubs.us
back
Brands availble:
Halvard Hubs Carbon
Ormo's
Tarvello
Rivosta
Dale Ferrow
Quorrin
Toplin Industries
Zelbrix
Ketro
Gandermark

```html
<!DOCTYPE html>
<html lang="en">
<head>
<meta charset="utf-8">
<title>Halvard Hubs Business Card</title>
<link href="https://fonts.googleapis.com/css2?family=Orbitron:wght@500;700&family=Michroma&display=swap" rel="stylesheet">
<style>
  :root {
    --backdrop: #2b2b2b;
    --card: #0b0b0b;
    --card-edge: #151515;
    --green: #2bf21f;
    --silver: #d6d6d6;
    --muted: #bdbdbd;
    --mark: #9a9a9a;
  }
  * { margin: 0; padding: 0; box-sizing: border-box; }
  html, body { width: 1200px; height: 1000px; overflow: hidden; }
  body { background: var(--backdrop); position: relative; font-family: "Michroma", sans-serif; }

  .card {
    position: absolute;
    left: 312px;
    width: 577px;
    height: 328px;
    overflow: hidden;
    background: radial-gradient(ellipse at 50% 40%, var(--card-edge) 0%, var(--card) 75%);
    box-shadow: 0 6px 18px rgba(0,0,0,0.55);
  }
  .card--front { top: 123px; }
  .card--back { top: 522px; }

  .brand-dot {
    position: absolute;
    left: 238px;
    top: 112px;
    width: 112px;
    height: 112px;
    border-radius: 50%;
    background: radial-gradient(circle at 40% 35%, #d8d8d8 0%, var(--mark) 70%);
  }
  .wordmark {
    position: absolute;
    top: 238px;
    left: 0; right: 0;
    text-align: center;
    font-family: "Orbitron", sans-serif;
    font-weight: 700;
    font-size: 29px;
    letter-spacing: 5px;
    color: var(--green);
    text-transform: uppercase;
  }
  .front-url {
    position: absolute;
    top: 282px;
    left: 0; right: 0;
    text-align: center;
    font-size: 10px;
    letter-spacing: 1.5px;
    color: var(--green);
    text-transform: uppercase;
  }

  .corner-dot {
    position: absolute;
    left: 455px;
    top: 212px;
    width: 140px;
    height: 140px;
    border-radius: 50%;
    background: radial-gradient(circle at 40% 35%, #8a8a8a 0%, #4a4a4a 75%);
  }

  .owner { position: absolute; left: 66px; top: 59px; }
  .owner__name {
    font-family: "Orbitron", sans-serif;
    font-weight: 500;
    font-size: 16px;
    letter-spacing: 4px;
    color: var(--silver);
    text-transform: uppercase;
  }
  .owner__role {
    font-size: 7px;
    letter-spacing: 1px;
    color: var(--green);
    text-transform: uppercase;
    margin-top: 0;
  }

  .contacts { position: absolute; left: 66px; top: 99px; list-style: none; }
  .contacts li {
    display: flex; align-items: center;
    height: 14px; margin-bottom: 11px;
    font-size: 8.5px; letter-spacing: 1px; color: var(--muted);
    text-transform: uppercase;
  }
  .contacts li.phone { font-size: 10px; letter-spacing: 1.5px; }
  .contacts svg { width: 14px; height: 12px; margin-right: 14px; fill: var(--green); }

  .brands { position: absolute; left: 45px; top: 208px; width: 400px; color: var(--green); text-transform: uppercase; font-size: 7.5px; letter-spacing: 0.8px; }
  .brands__title { margin-bottom: 12px; }
  .brands__row { position: relative; height: 21px; }
  .brands__row span { position: absolute; top: 0; white-space: nowrap; }
</style>
</head>
<body>
  <section class="card card--front">
    <div class="brand-dot" role="img" aria-label="Brand mark area"></div>
    <div class="wordmark">Halvard Hubs</div>
    <div class="front-url">www.halvardhubs.us</div>
  </section>

  <section class="card card--back">
    <div class="corner-dot" role="img" aria-label="Brand mark decoration"></div>
    <div class="owner">
      <div class="owner__name">Lemuel Castaby</div>
      <div class="owner__role">Owner/Builder</div>
    </div>
    <ul class="contacts">
      <li class="phone"><svg viewBox="0 0 14 12" aria-hidden="true"><path d="M1 4c0-2 3-3 6-3s6 1 6 3v1h-3V3.5C9 3 5 3 4 3.5V5H1z"/><rect x="3" y="6" width="8" height="5" rx="1"/></svg>555-418-7290</li>
      <li><svg viewBox="0 0 14 12" aria-hidden="true"><path d="M0 2h14v8H0z M1 3l6 4 6-4" fill="none" stroke="#2bf21f" stroke-width="1.4"/></svg>sales@halvardhubs.us</li>
      <li><svg viewBox="0 0 14 12" aria-hidden="true"><circle cx="7" cy="6" r="5.3" fill="none" stroke="#2bf21f" stroke-width="1.2"/><path d="M1.7 6h10.6M7 .7v10.6" stroke="#2bf21f" stroke-width="1"/><ellipse cx="7" cy="6" rx="2.4" ry="5.3" fill="none" stroke="#2bf21f" stroke-width="1"/></svg>www.halvardhubs.us</li>
    </ul>
    <div class="brands">
      <div class="brands__title">Brands availble:</div>
      <div class="brands__row"><span style="left:0">Halvard Hubs Carbon</span><span style="left:211px">Ormo's</span><span style="left:324px">Tarvello</span></div>
      <div class="brands__row"><span style="left:0">Rivosta</span><span style="left:120px">Dale Ferrow</span><span style="left:262px">Quorrin</span></div>
      <div class="brands__row"><span style="left:0">Toplin Industries</span><span style="left:183px">Zelbrix</span><span style="left:308px">Ketro</span></div>
      <div class="brands__row"><span style="left:113px">Gandermark</span></div>
    </div>
  </section>
</body>
</html>
```